Lip balm label

4 different kinds with a blend of essential oils. Cravings, Energy, Anxiety and Sensual. No preservatives or engineered products. Need different colored labels for each one. Maybe lavender or purple for stress, green or orange for appetite, red for energy and black for sensual. Or just use your professional judgement. Must fit on small lip balm tube

Target Market(s)

Young and old adults

Industry/Entity Type

Cosmetics

Logo Text

Mouthgrove

Logo styles of interest
Wordmark Logo
Font styles to use
Decorative

Requirements
Must have
• Name of company (KoRu Organics), 100% Organic, list of ingredients in each one, weight is 0.15 oz, made with Essential Oils, soothing and moisturizing,
• Lip Balm
Nice to have
• Made in USA, satisfaction guaranteed

```html
<!DOCTYPE html>
<html lang="en">
<head>
<meta charset="utf-8">
<title>Mouthgrove Lip Balm Label – Sensual Enhancement</title>
<link rel="stylesheet" href="https://fonts.googleapis.com/css2?family=PT+Sans+Narrow&family=Source+Sans+3:wght@400;600&family=Arimo&display=swap">
<style>
  :root {
    --page: #ffffff;
    --label-black: #000000;
    --gold: #a89063;
  }
  * { margin: 0; padding: 0; box-sizing: border-box; }
  html, body { width: 1200px; height: 1000px; overflow: hidden; background: var(--page); }
  .canvas { position: relative; width: 1200px; height: 1000px; }

  .label {
    position: absolute; left: 28px; top: 348px;
    width: 1144px; height: 294px;
    background: var(--label-black);
    color: var(--gold);
    font-family: "Source Sans 3", sans-serif;
  }
  .label__edge { position: absolute; top: 0; width: 22px; height: 100%; background: var(--gold); }
  .label__edge--left { left: 0; }
  .label__edge--right { right: 0; }

  .brand { position: absolute; left: 62px; top: 46px; width: 380px; text-align: center; }
  .brand__name { font-size: 62px; font-weight: 400; line-height: 1; letter-spacing: 0.5px; }
  .brand__sub { font-size: 22px; margin-top: 6px; padding-left: 80px; }

  .product { position: absolute; left: 458px; top: 56px; }
  .product__title {
    font-family: "PT Sans Narrow", sans-serif;
    font-size: 80px; font-weight: 400; line-height: 1; letter-spacing: -0.5px;
  }
  .product__claim { font-size: 16.5px; letter-spacing: 1px; margin-top: 12px; padding-left: 3px; }

  .company { position: absolute; left: 59px; top: 240px; font-size: 28px; line-height: 1; }

  .ingredients {
    position: absolute; left: 269px; top: 248px; width: 670px;
    font-family: "Arimo", sans-serif; font-size: 10px; line-height: 1.25;
  }

  .origin-badge {
    position: absolute; left: 955px; top: 247px; width: 104px; height: 28px;
    border: 1px solid var(--gold); border-radius: 6px; text-align: center;
  }
  .origin-badge__main { font-size: 11.5px; letter-spacing: 1px; line-height: 1; margin-top: 4px; }
  .origin-badge__sub { font-size: 7px; line-height: 1; margin-top: 1px; }

  .net-weight {
    position: absolute; left: 1100px; top: 245px;
    font-size: 17px; letter-spacing: 1px; line-height: 1;
    transform: translate(-50%, -50%) rotate(-90deg);
    transform-origin: center; white-space: nowrap;
  }
</style>
</head>
<body>
<div class="canvas">
  <section class="label">
    <div class="label__edge label__edge--left"></div>
    <div class="label__edge label__edge--right"></div>

    <div class="brand">
      <div class="brand__name">Mouthgrove</div>
      <div class="brand__sub">Essential Oils</div>
    </div>

    <div class="product">
      <h1 class="product__title">Sensual Enhancement</h1>
      <p class="product__claim">MADE WITH ESSENTIAL OILS, SOOTHING AND MOISTURIZING</p>
    </div>

    <div class="company">KoRu Organics</div>

    <p class="ingredients">Ingredients: Lorem ipsum dolor sit amet, consectetur adipiscing elit, sed do eiusmod tempor incididunt ut labore et dolore magna aliqua. Ut enim ad minim veniam, quis nostrud exercitation ullamco laboris nisi ut aliquip ex ea commodo consequat.</p>

    <div class="origin-badge">
      <div class="origin-badge__main">MADE IN USA</div>
      <div class="origin-badge__sub">Satisfaction guaranteed</div>
    </div>

    <div class="net-weight">0.15 oz</div>
  </section>
</div>
</body>
</html>
```